Clone http://www.velvorquillset.com/ (fully functioning WordPress website - not just design)

1) Clone or recreate http://www.velvorquillset.com/ in Wordpress with WooCommerece plugin
2) Connect to our Existing Quenz Account
3) Make site-wide text only changes that we provide you when site is complete.

We will provide all the graphics according to your size requirements.

Cash awarded to the closest copy of http://www.velvorquillset.com/

Target Market(s)

WordPress developer

Number of Pages Required

5+ page

Font styles to use
Sans Serif

Colors
abd037
cadf82
eaf2ce

Requirements
Must have
• Fully functioning website.

```html
<!DOCTYPE html>
<html lang="en">
<head>
<meta charset="utf-8">
<title>Velvorquill – Mail Merge Online</title>
<link href="https://fonts.googleapis.com/css2?family=Roboto:wght@300;400;500;700&display=swap" rel="stylesheet">
<style>
:root{
  --green-dark:#447a1f;
  --green:#4c8a26;
  --green-bright:#8dbb3a;
  --green-pale:#abd037;
  --grey-band:#efefef;
  --grey-panel:#e9e9e9;
  --text:#444;
  --text-soft:#777;
  --footer:#4a4a4a;
  --footer-base:#333;
  --white:#fff;
}
*{margin:0;padding:0;box-sizing:border-box}
html,body{width:1200px;height:2203px;overflow:hidden}
body{font-family:'Roboto',sans-serif;color:var(--text);background:var(--white);position:relative}
.abs{position:absolute}

/* top bar */
.topbar{left:0;top:0;width:1200px;height:28px;background:var(--green-dark);color:var(--white);font-size:10px;font-weight:700;letter-spacing:.3px}
.follow{left:161px;top:8px}
.dot{position:absolute;top:4px;width:20px;height:20px;border-radius:50%;background:var(--green-pale)}
.flag{left:826px;top:4px;width:34px;height:20px;background:linear-gradient(180deg,#c94040,#e8e8e8 50%,#c94040);border-radius:2px}
.login{left:868px;top:0;width:86px;height:28px;background:var(--green);font-size:9px;line-height:28px;padding-left:34px}
.register{left:954px;top:0;width:84px;height:28px;background:#6ea335;font-size:9px;line-height:28px;padding-left:32px}

/* header */
.header{left:0;top:28px;width:1200px;height:84px;background:var(--white);border-bottom:1px solid #e4e4e4}
.brand{left:161px;top:30px;font-size:19px;font-weight:500;color:var(--green);display:flex;align-items:center;gap:8px}
.brand i{width:14px;height:14px;border-radius:50%;background:var(--green-pale);display:block}
.nav{right:160px;top:36px;display:flex;gap:26px;font-size:10px;color:#666}
.nav .on{color:var(--green);border-bottom:2px solid var(--green);padding-bottom:8px}

/* hero */
.hero{left:0;top:112px;width:1200px;height:515px;background:linear-gradient(90deg,#1a0e07 0%,#4a2a14 40%,#7a4a22 70%,#3a200f 100%)}
.hero-img{left:400px;top:60px;width:760px;height:455px;background:radial-gradient(ellipse at 45% 50%,#b9b9b9 0%,#6a6a6a 30%,rgba(80,50,25,0) 60%)}
.hero h1{left:159px;top:258px;color:var(--white);font-weight:400;font-size:27px;line-height:1.1}
.hero h1 strong{display:block;font-weight:700;font-size:40px;margin-top:4px}
.hero p{left:161px;top:352px;width:340px;color:#eee;font-size:16px;font-weight:300;line-height:20px}
.btn-outline{border:2px solid var(--white);color:var(--white);font-size:11px;font-weight:700;text-align:center;line-height:38px}
.hero .btn-outline{left:161px;top:423px;width:153px;height:42px}

/* intro */
.intro{left:0;top:627px;width:1200px;height:110px;background:var(--grey-band);text-align:center}
.intro h2{margin-top:26px;color:var(--green);font-size:16px;font-weight:400}
.intro p{width:620px;margin:8px auto 0;font-size:11px;color:#666;line-height:15px}

.tagline{left:0;top:782px;width:1200px;text-align:center;font-size:29px;font-weight:300;color:#555;letter-spacing:.3px}

/* features */
.photo{width:600px;height:309px}
.panel{width:600px;height:309px;background:var(--grey-panel)}
.step{position:absolute;left:20px;top:38px;width:500px}
.step .num{position:absolute;left:0;top:0;width:58px;height:58px;border:3px solid var(--green);border-radius:50%;color:var(--green);font-size:28px;font-weight:500;text-align:center;line-height:52px}
.step h3{position:absolute;left:74px;top:12px;font-size:29px;font-weight:300;color:var(--green);white-space:nowrap}
.step h4{position:absolute;left:74px;top:77px;font-size:16px;font-weight:300;color:#555}
.step p{position:absolute;left:74px;top:112px;width:343px;font-size:10.5px;color:#666;line-height:20.5px}

/* cta */
.cta{left:0;top:1839px;width:1200px;height:122px;background:linear-gradient(90deg,#7fb43a,#95c24a 50%,#84b83d)}
.cta h2{left:241px;top:50px;color:var(--white);font-size:16px;font-weight:400}
.cta .btn-outline{left:705px;top:40px;width:183px;height:42px}

/* footer */
.footer{left:0;top:1961px;width:1200px;height:198px;background:var(--footer);color:#ccc;font-size:10px}
.footer h5{position:absolute;top:20px;font-size:11px;font-weight:500;color:var(--white);border-bottom:1px solid #888;padding-bottom:4px}
.footer .about{position:absolute;left:161px;top:135px;width:280px;line-height:13px}
.footer .fbrand{position:absolute;left:161px;top:72px;font-size:14px;color:#ddd;display:flex;gap:6px;align-items:center}
.footer .fbrand i{width:10px;height:10px;border-radius:50%;background:#bbb;display:block}
.links{position:absolute;top:62px;list-style:none;line-height:25.5px}
.links li::before{content:"›";margin-right:12px;color:#bbb}
.ic{position:absolute;width:20px;height:20px;border:1px solid #bbb;border-radius:50%}
.contact{position:absolute;left:806px;line-height:14px}
.social{position:absolute;top:156px;width:20px;height:20px;border-radius:50%;background:#bbb}
.base{left:0;top:2159px;width:1200px;height:44px;background:var(--footer-base);color:#bbb;font-size:9px;text-align:center;line-height:44px}
</style>
</head>
<body>

<div class="abs topbar">
  <span class="abs follow">FOLLOW US ON:</span>
  <span class="dot" style="left:252px"></span>
  <span class="dot" style="left:278px"></span>
  <span class="dot" style="left:303px"></span>
  <div class="abs flag" role="img" aria-label="Language flag"></div>
  <div class="abs login">
    <svg class="abs" style="left:15px;top:9px" width="9" height="10" viewBox="0 0 9 10"><rect x="0" y="4" width="9" height="6" fill="#fff"/><path d="M2 4V3a2.5 2.5 0 0 1 5 0v1" stroke="#fff" stroke-width="1.4" fill="none"/></svg>LOGIN
  </div>
  <div class="abs register">
    <svg class="abs" style="left:12px;top:9px" width="12" height="10" viewBox="0 0 12 10"><circle cx="4.5" cy="3" r="2.5" fill="#fff"/><path d="M0 10a4.5 4 0 0 1 9 0z" fill="#fff"/><path d="M10.5 3v4M8.5 5h4" stroke="#fff" stroke-width="1.2"/></svg>REGISTER
  </div>
</div>

<header class="abs header">
  <div class="abs brand"><i></i>Velvorquill</div>
  <nav class="abs nav">
    <span class="on">HOME</span><span>TOUR &#8964;</span><span>PRICE</span><span>OUR TEAM</span><span>CONTACT US</span>
  </nav>
</header>

<section class="abs hero">
  <div class="abs hero-img" role="img" aria-label="Laptop, notebook, pen, plant and a hand holding coffee on a wooden desk"></div>
  <h1 class="abs">LOREM IPSUM DOLOR SIT<strong>FUSCE BIBENDUM</strong></h1>
  <p class="abs">Pellentesque dolor tortor, lacinia in arcu eu, consectetur varius magna.</p>
  <div class="abs btn-outline">START A FREE TRAIL</div>
</section>

<section class="abs intro">
  <h2>Maecenas facilisis tristique eleifend. Proin in viverra leo, eu lobortis nibh?</h2>
  <p>Fusce bibendum luctus orci, eu consectetur nisi pharetra quis. Fusce condimentum metus nec dui aliquet facilisis sit amet eu nibh. Nunc dolor libero, gravida id enim ac, dictum imperdiet neque.</p>
</section>

<h2 class="abs tagline">100% EASIER THAN USING QUILLPAD WRITER!</h2>

<div class="abs photo" style="left:0;top:855px;background:linear-gradient(135deg,#e9b85c,#f0c874 50%,#d9a548)" role="img" aria-label="Letterhead, business cards, stamp and tape on a yellow surface"></div>
<div class="abs panel" style="left:600px;top:855px">
  <div class="step"><div class="num">1</div><h3>UPLOAD YOUR DATA</h3><h4>Pellentesque dolor tortor, lacinia in arcu eu</h4>
  <p>Lorem ipsum dolor sit amet, consectetur adipiscing elit. Nullam varius, mi ut rutrum mollis, justo ante imperdiet massa, eu tincidunt velit leo eget quam. Aliquam erat volutpat. Pellentesque faucibus facilisis augue nec aliquam. Fusce aliquet at lorem eu viverra. Orci varius natoque penatibus et magnis dis parturient montes, nascetur ridiculus mus. Etiam suscipit magna vel est aliquam, feugiat placerat velit elementum.</p></div>
</div>

<div class="abs panel" style="left:0;top:1164px">
  <div class="step" style="left:160px"><div class="num">2</div><h3>DESIGN YOUR TEMPLATE</h3><h4>Vestibulum laoreet purus ut lorem blandit</h4>
  <p>Lorem ipsum dolor sit amet, consectetur adipiscing elit. Nullam varius, mi ut rutrum mollis, justo ante imperdiet massa, eu tincidunt velit leo eget quam. Aliquam erat volutpat. Pellentesque faucibus facilisis augue nec aliquam. Fusce aliquet at lorem eu viverra. Orci varius natoque penatibus et magnis dis parturient montes, nascetur ridiculus mus. Etiam suscipit magna vel est aliquam, feugiat placerat velit elementum.</p></div>
</div>
<div class="abs photo" style="left:600px;top:1164px;background:radial-gradient(ellipse at 50% 50%,#3a2f4a 0%,#4a4f6a 25%,#a9dbe0 55%,#bfe6e6 100%)" role="img" aria-label="Tablet showing an app screen on a pale teal background"></div>

<div class="abs photo" style="left:0;top:1472px;background:radial-gradient(ellipse at 45% 50%,#f2f2f2 0%,#e8e8e8 35%,#2452b0 60%,#1f4aa6 100%)" role="img" aria-label="Printed sheet with a yellow headline on a blue background"></div>
<div class="abs panel" style="left:600px;top:1472px">
  <div class="step"><div class="num">3</div><h3>MERGE TO PDF</h3><h4>Maecenas facilisis tristique eleifend</h4>
  <p>Lorem ipsum dolor sit amet, consectetur adipiscing elit. Nullam varius, mi ut rutrum mollis, justo ante imperdiet massa, eu tincidunt velit leo eget quam. Aliquam erat volutpat. Pellentesque faucibus facilisis augue nec aliquam. Fusce aliquet at lorem eu viverra. Orci varius natoque penatibus et magnis dis parturient montes, nascetur ridiculus mus. Etiam suscipit magna vel est aliquam, feugiat placerat velit elementum.</p></div>
</div>

<section class="abs cta">
  <h2 class="abs">START BUILDING YOUR MAIL MERGE ONLINE NOW!</h2>
  <div class="abs btn-outline">START A FREE TRAIL NOW</div>
</section>

<footer class="abs footer">
  <h5 style="left:161px">ABOUT US</h5>
  <div class="fbrand"><i></i>Velvorquill</div>
  <p class="about">Lorem ipsum dolor sit amet, consectetur adipiscing elit. Nullam varius, mi ut rutrum mollis, justo ante imperdiet massa, eu tincidunt velit leo eget quam. Aliquam erat volutpat. Pellentesque faucibus facilisis augue nec aliquam.</p>

  <h5 style="left:463px">QUICK LINKS</h5>
  <ul class="links" style="left:463px"><li>Home</li><li>About us</li><li>Team</li><li>Tour</li><li>Price</li></ul>
  <ul class="links" style="left:593px"><li>Privacy Policy</li><li>Terms &amp; Conditions</li><li>Refund Policy</li></ul>

  <h5 style="left:762px">GET IN TOUCH</h5>
  <span class="ic" style="left:762px;top:62px"><svg width="18" height="18" viewBox="0 0 18 18"><path d="M9 4a3 3 0 0 1 3 3c0 2.5-3 6-3 6s-3-3.5-3-6a3 3 0 0 1 3-3z" fill="#ccc"/><circle cx="9" cy="7" r="1" fill="#4a4a4a"/></svg></span>
  <p class="contact" style="top:64px">Unit 14 Larkmoor Row<br>Fennick Bay</p>
  <span class="ic" style="left:762px;top:103px"><svg width="18" height="18" viewBox="0 0 18 18"><rect x="5" y="6" width="8" height="6" fill="#ccc"/><path d="M5 6l4 3 4-3" stroke="#4a4a4a" fill="none"/></svg></span>
  <p class="contact" style="top:107px">info@velvorquill-mail.com</p>
  <span class="social" style="left:762px"></span>
  <span class="social" style="left:787px"></span>
  <span class="social" style="left:812px"></span>
</footer>

<div class="abs base">© Copyright 2017 Test All Rights Reserved</div>

</body>
</html>
```